Western Canadian Survey Company needs Business Card and Letter Head Design

Hello,

We're looking to have our business cards redesigned along with our letterhead.

We've recently changed out logo and would like to use this. Please use some creativity and propose different options (Traditional and modern).

We will provide as much feedback as possible.

Business card should be double sided with our logo. We would also like room for cell phone number, email address and position. Back of the card can just be our logo or potentially a list of our services we provide.

Industry/Entity Type

Business

Contact Information for Business Card

```html
<!DOCTYPE html>
<html lang="en">
<head>
<meta charset="utf-8">
<title>Ridgeline Survey Group – Stationery</title>
<link href="https://fonts.googleapis.com/css2?family=Open+Sans:wght@400;600;700&display=swap" rel="stylesheet">
<style>
  :root {
    --bg: #dcdee0;
    --paper: #fbfbfb;
    --slate: #34495a;
    --slate-light: #6f8291;
    --ink: #2b2f33;
    --muted: #5a6168;
  }
  * { box-sizing: border-box; margin: 0; padding: 0; }
  html, body { width: 1200px; height: 960px; overflow: hidden; }
  body {
    background: var(--bg);
    font-family: "Open Sans", Arial, sans-serif;
    color: var(--ink);
    position: relative;
  }
  .sheet {
    position: absolute;
    background: var(--paper);
    box-shadow: 0 6px 18px rgba(0,0,0,0.12);
    overflow: hidden;
  }
  .top-accent { position: absolute; top: 0; height: 14px; }
  .bottom-band { position: absolute; left: 0; bottom: 0; width: 100%; }
  .web {
    position: absolute; right: 5%; color: #e8edf1;
    font-size: 9px; letter-spacing: 0.2px;
  }
  .brand { display: flex; align-items: center; gap: 8px; }
  .brand-mark { width: 14px; height: 14px; background: var(--slate); flex: none; }
  .brand-name {
    font-weight: 700; color: var(--slate); letter-spacing: 1.2px;
    text-transform: uppercase; white-space: nowrap;
  }
  .contact-list { list-style: none; }
  .contact-list li {
    display: flex; align-items: center; gap: 6px;
    color: var(--muted); line-height: 1;
  }
  .icon { width: 11px; height: 11px; flex: none; }

  /* Letterhead */
  .letterhead { left: 40px; top: 110px; width: 520px; height: 735px; }
  .letterhead .top-accent { left: 54%; width: 42%; }
  .letterhead .brand { position: absolute; top: 66px; left: 0; width: 100%; justify-content: center; }
  .letterhead .brand-name { font-size: 17px; }
  .letter-body {
    position: absolute; top: 118px; left: 62px; right: 62px;
    font-size: 10.5px; line-height: 1.55; text-align: justify; color: var(--ink);
  }
  .letter-body p { text-indent: 2em; margin-bottom: 8px; }
  .letterhead .contact-list { position: absolute; left: 40px; bottom: 66px; }
  .letterhead .contact-list li { font-size: 9px; margin-top: 5px; }
  .letterhead .bottom-band { height: 42px; }
  .letterhead .web { bottom: 9px; font-size: 10px; }

  /* Business cards */
  .card { width: 340px; height: 194px; left: 620px; }
  .card .top-accent { left: 52%; width: 44%; height: 10px; }
  .card .bottom-band { height: 24px; }
  .card .web { bottom: 4px; font-size: 8px; }
  .card-logo { top: 110px; }
  .card-logo .brand { position: absolute; top: 78px; left: 0; width: 100%; justify-content: center; }
  .card-logo .brand-name { font-size: 15px; }

  .card-details { top: 328px; }
  .card-details .person { position: absolute; left: 22px; top: 26px; }
  .person-name { font-size: 11px; font-weight: 700; color: var(--ink); }
  .person-role { font-size: 8.5px; color: var(--muted); margin-top: 1px; }
  .card-details .brand { position: absolute; right: 20px; top: 32px; gap: 6px; }
  .card-details .brand-mark { width: 10px; height: 10px; }
  .card-details .brand-name { font-size: 10.5px; letter-spacing: 0.8px; }
  .card-details .contact-list { position: absolute; left: 22px; top: 80px; }
  .card-details .contact-list li { font-size: 8px; margin-top: 6px; }
  .card-address {
    position: absolute; right: 20px; top: 104px;
    display: flex; align-items: flex-start; gap: 6px;
    font-size: 8px; color: var(--muted); text-align: right; line-height: 1.45;
  }

  /* Envelope */
  .envelope { left: 620px; top: 560px; width: 540px; height: 257px; }
  .envelope .brand { position: absolute; left: 34px; top: 34px; }
  .envelope .brand-name { font-size: 15px; }
  .envelope .contact-list { position: absolute; left: 34px; top: 84px; }
  .envelope .contact-list li { font-size: 9px; margin-top: 6px; }
  .envelope .bottom-band { height: 30px; }
  .envelope .web { bottom: 6px; }
</style>
</head>
<body>

<svg width="0" height="0" style="position:absolute">
  <defs>
    <symbol id="ico-phone" viewBox="0 0 12 12">
      <rect width="12" height="12" rx="2" fill="#34495a"/>
      <path d="M4 2.5h1.2l.6 2-1 .7a5 5 0 0 0 2 2l.7-1 2 .6V8a1 1 0 0 1-1 1A6 6 0 0 1 3 3.5a1 1 0 0 1 1-1z" fill="#fff"/>
    </symbol>
    <symbol id="ico-mail" viewBox="0 0 12 12">
      <rect width="12" height="12" rx="2" fill="#34495a"/>
      <rect x="2.5" y="3.5" width="7" height="5" fill="none" stroke="#fff" stroke-width="1"/>
      <path d="M2.5 3.5 6 6.5l3.5-3" fill="none" stroke="#fff" stroke-width="1"/>
    </symbol>
    <symbol id="ico-pin" viewBox="0 0 12 12">
      <rect width="12" height="12" rx="2" fill="#34495a"/>
      <path d="M6 2.2a2.6 2.6 0 0 1 2.6 2.6C8.6 6.8 6 9.8 6 9.8S3.4 6.8 3.4 4.8A2.6 2.6 0 0 1 6 2.2z" fill="#fff"/>
      <circle cx="6" cy="4.8" r="1" fill="#34495a"/>
    </symbol>
    <symbol id="band" viewBox="0 0 1000 40" preserveAspectRatio="none">
      <polyline points="0,12 594,12 618,1 1000,1" fill="none" stroke="#6f8291" stroke-width="1.5" vector-effect="non-scaling-stroke"/>
      <polygon points="0,18 600,18 625,6 1000,6 1000,40 0,40" fill="#34495a"/>
    </symbol>
    <symbol id="accent" viewBox="0 0 1000 14" preserveAspectRatio="none">
      <polygon points="0,0 1000,0 1000,14 970,4 0,4" fill="#34495a"/>
    </symbol>
  </defs>
</svg>

<!-- Letterhead -->
<section class="sheet letterhead">
  <svg class="top-accent" preserveAspectRatio="none"><use href="#accent" width="100%" height="100%"/></svg>
  <div class="brand"><span class="brand-mark"></span><span class="brand-name">Ridgeline Survey Group</span></div>
  <div class="letter-body">
    <p>Lorem ipsum dolor sit amet, consectetur adipiscing elit. Donec orci purus, luctus vitae dignissim eu, iaculis sed purus. Vivamus faucibus, ipsum nec aliquet viverra, leo mauris condimentum ligula, sit amet sagittis enim ligula quis arcu. Nam egestas tortor id nisi porttitor mattis. In tortor ante, ultricies in suscipit a, tempus non massa. Vivamus et auctor mi. Fusce vel massa nulla. Phasellus nec eros mauris, et scelerisque orci.</p>
    <p>Donec malesuada orci vitae nulla accumsan porta a id massa. Quisque accumsan iaculis magna sit amet fringilla. Maecenas consequat, magna eget tincidunt semper, odio nibh rutrum mi, id feugiat ante nisi eu risus. Vestibulum nunc orci, rhoncus a placerat in, ultricies in mi. Cras mattis varius eros, vel fringilla nisi suscipit eget. Quisque scelerisque sagittis nulla at porttitor.</p>
    <p>Sed id augue vitae urna euismod commodo aliquet a quam. Pellentesque arcu velit, cursus et malesuada ut, consequat et diam. Nullam erat sem, rhoncus id ullamcorper vitae, rhoncus et arcu. In ultricies ultricies nulla, ut pretium magna. Aliquam magna a metus ornare faucibus. Fusce aliquet faucibus lectus, vitae dignissim nunc tincidunt gravida, sem arcu adipiscing lacus, ac laoreet nisi nunc vitae dui. Quisque nec diam sed risus consectetur a ccumsan sit amet ut elit. Donec a purus lorem.</p>
  </div>
  <ul class="contact-list">
    <li><svg class="icon"><use href="#ico-phone"/></svg>+000 4821 7365</li>
    <li><svg class="icon"><use href="#ico-mail"/></svg>mail@ridgelinesurvey.com</li>
    <li><svg class="icon"><use href="#ico-pin"/></svg>Harlow Court, Birch Lane, Westbrook B 2210</li>
  </ul>
  <svg class="bottom-band" preserveAspectRatio="none"><use href="#band" width="100%" height="100%"/></svg>
  <span class="web">www.ridgelinesurvey.com</span>
</section>

<!-- Business card: logo side -->
<section class="sheet card card-logo">
  <svg class="top-accent" preserveAspectRatio="none"><use href="#accent" width="100%" height="100%"/></svg>
  <div class="brand"><span class="brand-mark"></span><span class="brand-name">Ridgeline Survey Group</span></div>
  <svg class="bottom-band" preserveAspectRatio="none"><use href="#band" width="100%" height="100%"/></svg>
  <span class="web">www.ridgelinesurvey.com</span>
</section>

<!-- Business card: details side -->
<section class="sheet card card-details">
  <div class="person">
    <div class="person-name">Mr. Your Name</div>
    <div class="person-role">Designation</div>
  </div>
  <div class="brand"><span class="brand-mark"></span><span class="brand-name">Ridgeline Survey Group</span></div>
  <ul class="contact-list">
    <li><svg class="icon"><use href="#ico-phone"/></svg>+000 4821 7365</li>
    <li><svg class="icon"><use href="#ico-mail"/></svg>mail@ridgelinesurvey.com</li>
  </ul>
  <div class="card-address">
    <span>Harlow Court, Birch Lane,<br>Westbrook B 2210</span>
    <svg class="icon"><use href="#ico-pin"/></svg>
  </div>
  <svg class="bottom-band" preserveAspectRatio="none"><use href="#band" width="100%" height="100%"/></svg>
</section>

<!-- Envelope -->
<section class="sheet envelope">
  <div class="brand"><span class="brand-mark"></span><span class="brand-name">Ridgeline Survey Group</span></div>
  <ul class="contact-list">
    <li><svg class="icon"><use href="#ico-phone"/></svg>+000 4821 7365</li>
    <li><svg class="icon"><use href="#ico-mail"/></svg>mail@ridgelinesurvey.com</li>
    <li><svg class="icon"><use href="#ico-pin"/></svg>Harlow Court, Birch Lane, Westbrook B 2210</li>
  </ul>
  <svg class="bottom-band" preserveAspectRatio="none"><use href="#band" width="100%" height="100%"/></svg>
  <span class="web">www.ridgelinesurvey.com</span>
</section>

</body>
</html>
```